Race car follow-up website needs web design

We are currently finalising a website which allows amateur and professional owners of race cars to track the running time of the car and all installed parts (drive shafts, gearbox etc.). The site is working for a technical point of view, but needs a nice design applied to it.

The website is made with Bootstrap 3.x and does not need a mobile skin. We target desktop and tablet users. This means that the delivered work should be easy to incorporate in the Bootstrap site that currently exists, from a technical point of view.

In attachment you can find all the screens that need skinning. If you think some stuff can be done better from a usability or design point of view (size of tables, placement of buttons etc.), do not hesitate to make a suggestion. We are open to positive criticism, and the current "base" design is not carved in stone. The colors currently used are basic Bootstrap so that can change too. There are no limits whatsoever, as long as the result looks good.

We have a big amount of racing/racecar/mechanic/pitbox related photo material that can be used, so do not hesitate to ask for material if needed.

The start page should be something along the lines of these sites:

https://plumvex.me/
http://quorvane.io/
https://teldrova.com/
http://www.mivostrel.com/

Or in words: a top navigation bar (as seen in the screenshots). A full-width image relevant to the content (racing related) with some text in overlay (A sort of slogan along the lines of "Let us track your parts" or "Parts tracking for you race or trackday car" ). Under that image there should then be a very high-level overview of what the website can be used for (In a few steps, with graphics/photos, schematics, showing driving the car, data transfer, management in the site.). This so the potential user can quickly see if it is of any interest to him/her.

Basically:

Drive --- Download data -- Get Alerted

each step should contain an "icon" representing what it is about, and a few lines of text explaining what is meant.

On that page (in the image part, or below the explanation) there should be 2 links (buttons). One leads to the pricing page, one to the registration page.

Of course this first page cannot be finalised until we give the complete details of the content, so please provide a high-level design and the person I work with will receive the detailed specs (the text for the different steps etc).

The other screens are (we think) self-explanatory. Please look at them in chronological order (they are prefixed 00 to 19)

There are screenshots of the manual. This page will also need to be styled (to match the rest of the site and to make the layout a bit more sexy). We will of course provide the original html file to this once the content needs to be finalised.

Besides the website, a mail template is required too. The site sends mails for:
- registration confirmation
- lost password
- alerts related to the car parts or the data files.

These mails should also have a professional looking skin (right now they are plain text)

Just to make things clear, if you think the base design we made is "crap", please suggest improvements (for instance, menu placement in the bottom, positioning of certain elements, tables that might be better off somewhere else, the car details on top that take too much screen real-estate etc. etc.). This site has been built by developers, not by designers. The only condition is that it should be technically possible in a reasonable amount of time using Bootstrap 3.x

Please provide the resources in such a way that a developer with web skills can directly implement them. So any slicing of graphics should be done by the designer. If you only provide us a good looking psd file we won't be able to do anything with that, unfortunately.

If you, as a designer, have a passion for sports cars, race cars, trackdays and/or GT car racing, this is of course a plus. The collaboration will be a lot easier if we speak the same "language".

Please provide at least a design of
- the start page
- the "car details" page
- one of the list modals
- one of the form modals

so we can at least know how the rest of the pages will look

The name is Pitlane Ledger.

Some pictures that can be used:

https://www.snapvelo.com/photos/58310472@K04/20581937466/
https://www.snapvelo.com/photos/58310472@K04/4815209367/
https://www.snapvelo.com/photos/58310472@K04/4812766058/
https://www.snapvelo.com/photos/58310472@K04/4801533729/
https://www.snapvelo.com/photos/58310472@K04/4763921850/
https://www.snapvelo.com/photos/58310472@K04/4706418592/
https://www.snapvelo.com/photos/58310472@K04/4594071683/
https://www.snapvelo.com/photos/58310472@K04/4361829074/
https://www.snapvelo.com/photos/58310472@K04/3958316247/
https://www.snapvelo.com/photos/58310472@K04/3927140568/
https://www.snapvelo.com/photos/58310472@K04/3915762839/
https://www.snapvelo.com/photos/58310472@K04/3915764901/
https://www.snapvelo.com/photos/58310472@K04/3890417352/
https://www.snapvelo.com/photos/58310472@K04/3885093716/
https://www.snapvelo.com/photos/58310472@K04/3885097284/
https://www.snapvelo.com/photos/58310472@K04/2081359647/
https://www.snapvelo.com/photos/58310472@K04/2398640513/
https://www.snapvelo.com/photos/58310472@K04/2486075129/
https://www.snapvelo.com/photos/58310472@K04/2323149876/
https://www.snapvelo.com/photos/58310472@K04/2323154902/

Basically you take whatever you want from this guy’s photo stream:
https://www.snapvelo.com/photos/58310472@K04/

I know him personally so there should be no copyright issues.

Most users of the site will run so called "GT" cars (Valdorni, Castruzzo etc.), so please refrain from using (or referencing) open wheelers, F1, LMP etc.

There is a logo contest too: http://gigs.pixelbazaar.com/gig.aspx?id=837461

I just updated the brief with some more info and images you can use.

I have updated the brief. This is added: for the first screen, the schematics are explained in a bit more detail: Basically: Drive ---> Download data --> Get Alerted each step should contain an "icon" representing what it is about, and a few lines of text explaining what is meant.

Dear designers, As we have received numerous remarks about our contest from you and your colleagues we have contacted PixelBazaar to solve the situation. This contest will be split into two different contests. One logo design contest for $400 and one website design contest for the $1480. Everyone who has submitted logos can of course participate with those logos in the logo design contest (there are a few that we like, which have been submitted). We are very sorry for the inconvenience we might have caused, and if you want to redraw your designs already submitted because of this we will fully understand this, but we hope this decision will make things clearer for everyone participating. As soon as matters are changed we will send you all a new message with the updated information. Thanks for your understanding. Morlek BVBA

The logo contest has been created: http://gigs.pixelbazaar.com/gig.aspx?id=837461

Reason: Because of the split in webdesign / logo the deadline has been extended so non-logo webdesigners can participate too. Logo project: http://gigs.pixelbazaar.com/gig.aspx?id=837461

The pricing page has been added in the screenshots section

Trackday enthousiasts, race car owners, race teams.

• No video
No huge "footer" with a lot of links to navigate the site, since there will be very litte content.
No references to non-GT type cars (so no F1, no Series Quelmont, no LMP1/LMP2) or street cars.

```html
<!DOCTYPE html>
<html lang="en">
<head>
<meta charset="utf-8">
<title>Pitlane Ledger – Select Car</title>
<link rel="stylesheet" href="https://fonts.googleapis.com/css2?family=Open+Sans:wght@400;600&family=Questrial&display=swap">
<style>
:root{
  --red:#c40000;
  --red-deep:#8e0a0a;
  --ink:#222;
  --muted:#555;
  --header-bg:#f2f2f2;
  --page-bg:#ffffff;
  --footer-bg:#2a2a2a;
  --table-head:#3b3b3b;
  --row-tint:#fff0f0;
  --grey-btn:#4a4a4a;
}
*{box-sizing:border-box;margin:0;padding:0}
html,body{width:1151px;height:1200px;overflow:hidden}
body{position:relative;background:var(--page-bg);font-family:"Open Sans",sans-serif;color:var(--ink)}

.site-header{position:absolute;top:0;left:0;width:1151px;height:102px;background:var(--header-bg);border-bottom:2px solid var(--red)}
.brand{position:absolute;left:108px;top:28px;display:flex;align-items:center;gap:16px}
.brand-dot{width:66px;height:66px;border-radius:50%;background:var(--red-deep)}
.brand-name{font-family:"Questrial",sans-serif;font-size:36px;color:#333}
.user-bar{position:absolute;left:652px;top:0;width:393px;height:38px;background:#e4e4e4;border-radius:0 0 20px 20px;font-size:14px;color:#777}
.user-bar .select{position:absolute;left:22px;top:10px}
.user-bar .user{position:absolute;left:215px;top:10px}
.caret{display:inline-block;width:0;height:0;border-left:6px solid transparent;border-right:6px solid transparent;border-top:7px solid #999;margin-left:6px;vertical-align:1px}
.logout{position:absolute;left:950px;top:3px;width:71px;height:32px;background:var(--red);color:#fff;font-size:14px;line-height:32px;text-align:center;border-radius:3px}
.main-nav{position:absolute;left:516px;top:76px;display:flex;gap:39px;font-size:14px;color:#555;text-transform:uppercase}
.main-nav .active{color:var(--red);font-weight:600}

.hero{position:absolute;top:102px;left:0;width:1151px;height:500px;background:linear-gradient(180deg,#6b6b6b 0%,#3c3c3c 55%,#8a8a8a 100%)}
.hero-arrow{position:absolute;top:258px;width:40px;height:40px;border-radius:50%;background:#d8d8d8}
.hero-arrow svg{display:block;margin:11px auto}

.features{position:absolute;top:602px;left:0;width:1151px;height:496px;background:var(--page-bg)}
.feature{position:absolute;top:100px;width:240px;text-align:center}
.feature-icon{height:34px}
.feature-title{margin-top:20px;font-size:21px;font-weight:400;color:#1a1a1a}
.feature-text{margin-top:18px;font-size:13px;line-height:19.2px;color:#333}
.read-more{display:inline-block;margin-top:28px;width:96px;height:31px;line-height:31px;background:var(--red-deep);color:#f3c0c0;font-size:13px;border-radius:2px}

.site-footer{position:absolute;top:1098px;left:0;width:1151px;height:102px;background:var(--footer-bg);color:#bbb}
.newsletter-title{position:absolute;left:111px;top:14px;font-size:19px;color:#ccc}
.newsletter-form{position:absolute;left:110px;top:49px;width:220px;height:31px;border:1px solid #666;border-radius:3px;display:flex;overflow:hidden}
.newsletter-form .field{flex:1;background:#3a3a3a;color:#888;font-size:11px;font-style:italic;padding:8px 16px}
.newsletter-form .go{width:82px;background:var(--red);color:#fff;font-size:15px;font-weight:600;text-align:center;line-height:29px}
.copyright{position:absolute;right:121px;top:40px;font-size:12px;color:#aaa;text-align:right;line-height:23px}

.backdrop{position:absolute;top:102px;left:0;width:1151px;height:1098px;background:rgba(0,0,0,.47)}

.modal{position:absolute;left:259px;top:197px;width:585px;height:410px;background:#fff;border-radius:3px}
.modal-title{text-align:center;margin-top:29px;font-size:22px;font-weight:400;color:var(--red)}
.car-table{position:absolute;left:2px;top:81px;width:581px;border-collapse:collapse;font-size:13px;color:#666}
.car-table th{height:38px;background:var(--table-head);color:#fff;font-size:16px;font-weight:600;text-align:left;padding-left:12px;border-right:1px solid #555}
.car-table th:first-child{padding-left:11px}
.car-table td{height:48px;padding-left:27px;border-right:1px solid #e5e5e5}
.car-table td:first-child{padding-left:27px}
.car-table td:last-child,.car-table th:last-child{border-right:none}
.car-table tr:nth-child(even) td{background:var(--row-tint)}
.modal-actions{position:absolute;top:342px;left:0;width:100%;display:flex;justify-content:center;gap:7px}
.btn{height:32px;line-height:32px;padding:0 12px;color:#fff;font-size:14px;border-radius:3px;white-space:nowrap;text-align:center}
.btn-add{background:var(--red)}
.btn-cancel{background:var(--grey-btn)}
</style>
</head>
<body>

<header class="site-header">
  <div class="brand">
    <span class="brand-dot"></span>
    <span class="brand-name">Pitlane Ledger</span>
  </div>
  <div class="user-bar">
    <span class="select">Select Car<span class="caret"></span></span>
    <span class="user">Milan<span class="caret"></span></span>
  </div>
  <span class="logout">LOG OUT</span>
  <nav class="main-nav">
    <span class="active">Who we are</span>
    <span>What we do</span>
    <span>Our team</span>
    <span>Blog</span>
    <span>Contact us</span>
  </nav>
</header>

<section class="hero" role="img" aria-label="Photo of a GT race car on track, seen from the rear three-quarter">
  <span class="hero-arrow" style="left:26px"><svg width="18" height="18" viewBox="0 0 18 18"><path d="M12 2 5 9l7 7" fill="none" stroke="#333" stroke-width="3"/></svg></span>
  <span class="hero-arrow" style="left:1072px"><svg width="18" height="18" viewBox="0 0 18 18"><path d="M6 2l7 7-7 7" fill="none" stroke="#333" stroke-width="3"/></svg></span>
</section>

<section class="features">
  <div class="feature" style="left:133px">
    <div class="feature-icon"><svg width="30" height="30" viewBox="0 0 30 30"><circle cx="15" cy="17" r="10" fill="none" stroke="#555" stroke-width="2.5"/><path d="M15 17V10M15 17l-4 3M13 3h4M22 8l2-2" fill="none" stroke="#555" stroke-width="2.5"/></svg></div>
    <h3 class="feature-title">Track the Running Time</h3>
    <p class="feature-text">Cras ut porta ipsum. Fusce sapien ante, tristique non cursus in, tincidunt eget felis. Mauris velit dui, vestibulum et urna ac, adipiscing vestibulum dolor. Aenean sed arcu ac quam euismod eleifend in et felis.</p>
    <span class="read-more">READ MORE</span>
  </div>
  <div class="feature" style="left:453px">
    <div class="feature-icon"><svg width="32" height="32" viewBox="0 0 32 32"><g fill="#222"><circle cx="16" cy="16" r="10"/><rect x="13" y="1" width="6" height="30" rx="1"/><rect x="1" y="13" width="30" height="6" rx="1"/><rect x="13" y="1" width="6" height="30" rx="1" transform="rotate(45 16 16)"/><rect x="13" y="1" width="6" height="30" rx="1" transform="rotate(-45 16 16)"/></g><circle cx="16" cy="16" r="4.5" fill="#fff"/></svg></div>
    <h3 class="feature-title">Track The Installed Parts</h3>
    <p class="feature-text">Cras ut porta ipsum. Fusce sapien ante, tristique non cursus in, tincidunt eget felis. Mauris velit dui, vestibulum et urna ac, adipiscing vestibulum dolor. Aenean sed arcu ac quam euismod eleifend in et felis.</p>
    <span class="read-more">READ MORE</span>
  </div>
  <div class="feature" style="left:770px">
    <div class="feature-icon"><svg width="30" height="30" viewBox="0 0 30 30"><g fill="#555"><path d="M15 2 7 11h5v9h6v-9h5z"/><path d="M3 19h3v6h18v-6h3v9H3z"/></g></svg></div>
    <h3 class="feature-title">Update Your Car Parts</h3>
    <p class="feature-text">Cras ut porta ipsum. Fusce sapien ante, tristique non cursus in, tincidunt eget felis. Mauris velit dui, vestibulum et urna ac, adipiscing vestibulum dolor. Aenean sed arcu ac quam euismod eleifend in et felis.</p>
    <span class="read-more">READ MORE</span>
  </div>
</section>

<footer class="site-footer">
  <h4 class="newsletter-title">Newsletter</h4>
  <div class="newsletter-form"><span class="field">Email</span><span class="go">Subscribe</span></div>
  <div class="copyright">© 2014 Pitlane Ledger, All rights reserved<br>X2</div>
</footer>

<div class="backdrop"></div>

<div class="modal" role="dialog" aria-label="Select Car">
  <h2 class="modal-title">Select Car</h2>
  <table class="car-table">
    <colgroup><col style="width:73px"><col style="width:98px"><col style="width:137px"><col style="width:121px"><col></colgroup>
    <thead><tr><th>Index</th><th>Make</th><th>Model</th><th>Remarks</th><th>Owners</th></tr></thead>
    <tbody>
      <tr><td>1</td><td>Harlow</td><td>R52 K7 GTR</td><td>FSA</td><td>milan@pitmail.net</td></tr>
      <tr><td>2</td><td>Solvik</td><td>T47</td><td></td><td>milan@pitmail.net</td></tr>
      <tr><td>3</td><td>Harlow</td><td>2</td><td></td><td>milan@pitmail.net</td></tr>
      <tr><td>4</td><td>XC</td><td>xx</td><td></td><td>milan@pitmail.net</td></tr>
    </tbody>
  </table>
  <div class="modal-actions">
    <span class="btn btn-add">ADD CAR</span>
    <span class="btn btn-cancel">CANCEL</span>
  </div>
</div>

</body>
</html>
```